Shooting Supplies Business Card and Website Homepage Banner

We need to update the design on our current business card and Home Page.

Currently the design on our business card is the same as the Banner on our home page. We would like to keep this approach and thus this project is for both.

Our website is: www.kr-rangegearco.com.au

We would like to keep the images generic in as much as they appeal to all of our customers who are both male and female and shoot a variety of competition handguns.

We would like to still empathise our motto: Quality. Precision. Results. However the other wording (Be the best you can be with the right gear at the right price) needs to be removed.

We do not sell any firearms or firearm parts but obviously this does not effect having a firearm or part of a firearm in the graphic (preferably the supplied pistol photo) .

The picture attached of a firearm is actually personally owned by us so no copyright issues.

Please note the original business card was produced before we had our 1300 472 913 number and this needs to be on the card. Please refer to "Must Have Priorities".

We supply mainly Global Tactical Marksman Federation (GTMF) compliant equipment so please no pictures of generic guns, pistols, rifles etc etc.

If you can use a close up of the gun in the picture we attached that would be great. If you can keep the wording on the slide out of view (needs to be generic) that would help to as Vantage is directly related to HRW guns.

Please produce two versions of the same graphic : Standard Business Card Size and a Banner for the webpage - 726 x 277 px.

Target Market(s)

Male and female of all ages.

Top level competitors are very serious about their sport and spend hundreds of hours practicing and ensuring their guns run flawlessly.

Industry/Entity Type

Gun

Font styles to use
Serif
Sans Serif

Colors

Designer to choose colors to be used in the design.

Requirements
Must have
• Business Card must display the following information:

Website address: www.kr-rangegearco.com.au
Contact phone number: Australia 1300 472 913
Contact phone number: International +61 (0) 400 318 745
Contact email: info@kr-rangegearco.com.au
Fax: +61 (0) 8 9153 2867

This can be a high cost sport so competitors are looking for quality and the business card and web banner needs to portray professionalism, trust and quality.
Nice to have
• Close up of the supplied photo of pistol as a background
Should not have
• Original image of women shooting
Non GTMF imagery
Showing "Vantage" on the slide of the pistol

```html
<!DOCTYPE html>
<html lang="en">
<head>
<meta charset="utf-8">
<title>Kyle Reeves Shooting Supplies – Business Card</title>
<link rel="stylesheet" href="https://fonts.googleapis.com/css2?family=Arimo:wght@400;700&display=swap">
<style>
  :root {
    --bg: #cfd0d2;
    --black: #0d0d0e;
    --charcoal: #232427;
    --white: #f4f4f4;
    --silver: #c9cacc;
    --steel-light: #dcdde0;
    --steel-dark: #3a3c40;
    --orange: #f2a81d;
    --grey-text: #9a9b9e;
    --ink: #111111;
  }
  * { box-sizing: border-box; margin: 0; padding: 0; }
  html, body {
    width: 1200px; height: 900px; overflow: hidden;
    background: var(--bg);
    font-family: "Arimo", Arial, sans-serif;
  }
  .canvas {
    width: 1200px; height: 900px;
    display: flex; flex-direction: column; align-items: center; justify-content: center;
    gap: 50px;
  }
  .card {
    position: relative;
    width: 620px; height: 355px;
    overflow: hidden;
    box-shadow: 0 6px 18px rgba(0,0,0,.25);
  }

  /* ---------- Back of card: contact details ---------- */
  .card-back { background: var(--white); }
  .card-back .header-band { position: absolute; inset: 0; }
  .card-back .brand {
    position: absolute; right: 40px; top: 20px;
    display: flex; align-items: center; gap: 12px;
  }
  .brand-dot {
    width: 34px; height: 34px; border-radius: 50%;
    background: var(--orange);
  }
  .brand-name {
    color: var(--silver); font-weight: 400;
    line-height: 1.0; text-align: left;
  }
  .card-back .brand-name { font-size: 26px; }
  .card-back .brand-name span { display: block; font-size: 15px; letter-spacing: 2px; }
  .card-back .website {
    position: absolute; left: 170px; top: 96px;
    color: var(--grey-text); font-size: 14px;
  }
  .contact-list {
    list-style: none;
    position: absolute; left: 54px; top: 150px;
    display: flex; flex-direction: column; gap: 13px;
  }
  .contact-item {
    display: flex; align-items: center; gap: 14px;
    font-weight: 700; font-size: 17px; color: var(--ink);
  }
  .contact-icon {
    width: 26px; height: 26px; border-radius: 50%;
    background: var(--orange);
    display: flex; align-items: center; justify-content: center;
  }

  /* ---------- Front of card: brand ---------- */
  .card-front { background: var(--black); }
  .pistol-photo {
    position: absolute; inset: 0;
    background:
      radial-gradient(ellipse 45% 60% at 80% 20%, #5c6066 0%, #2d2f33 70%, transparent 100%),
      linear-gradient(125deg, var(--steel-light) 0%, #a9abaf 22%, #6d7075 40%, var(--steel-dark) 58%, var(--charcoal) 75%);
  }
  .front-shade { position: absolute; inset: 0; }
  .tagline {
    position: absolute; left: 200px; top: 206px;
    color: #ffffff; font-weight: 700; font-size: 20px;
  }
  .card-front .brand {
    position: absolute; left: 200px; top: 240px;
    display: flex; align-items: center; gap: 16px;
  }
  .card-front .brand-dot { width: 64px; height: 64px; }
  .card-front .brand-name { font-size: 46px; }
  .card-front .brand-name span { display: block; font-size: 21px; letter-spacing: 3px; margin-top: 4px; }
</style>
</head>
<body>
<main class="canvas">

  <!-- Contact side -->
  <section class="card card-back" aria-label="Business card, contact side">
    <svg class="header-band" width="620" height="355" viewBox="0 0 620 355" aria-hidden="true">
      <defs>
        <linearGradient id="bandGrad" x1="0" y1="0" x2="0" y2="1">
          <stop offset="0" stop-color="#2a2b2e"/>
          <stop offset="1" stop-color="#0b0b0c"/>
        </linearGradient>
      </defs>
      <path d="M0 0 H620 V95 Q310 150 0 95 Z" fill="url(#bandGrad)"/>
      <path d="M0 95 Q310 150 620 95" fill="none" stroke="#b9babd" stroke-width="3"/>
      <path d="M0 330 Q310 290 620 330 V355 H0 Z" fill="#1a1b1d"/>
      <path d="M0 330 Q310 290 620 330" fill="none" stroke="#b9babd" stroke-width="2"/>
    </svg>
    <div class="brand">
      <div class="brand-dot"></div>
      <p class="brand-name">Kyle Reeves<span>SHOOTING SUPPLIES</span></p>
    </div>
    <p class="website">www.kr-rangegearco.com.au</p>
    <ul class="contact-list">
      <li class="contact-item">
        <span class="contact-icon"><svg width="14" height="14" viewBox="0 0 24 24"><path d="M6.6 10.8a15 15 0 006.6 6.6l2.2-2.2c.3-.3.7-.4 1-.2 1.1.4 2.3.6 3.6.6.6 0 1 .4 1 1V20c0 .6-.4 1-1 1A17 17 0 013 4c0-.6.4-1 1-1h3.5c.6 0 1 .4 1 1 0 1.3.2 2.5.6 3.6.1.3 0 .7-.2 1z" fill="#222"/></svg></span>
        Australia 1300 472 913
      </li>
      <li class="contact-item">
        <span class="contact-icon"><svg width="14" height="14" viewBox="0 0 24 24"><path d="M6.6 10.8a15 15 0 006.6 6.6l2.2-2.2c.3-.3.7-.4 1-.2 1.1.4 2.3.6 3.6.6.6 0 1 .4 1 1V20c0 .6-.4 1-1 1A17 17 0 013 4c0-.6.4-1 1-1h3.5c.6 0 1 .4 1 1 0 1.3.2 2.5.6 3.6.1.3 0 .7-.2 1z" fill="#222"/></svg></span>
        International +61 (0) 400 318 745
      </li>
      <li class="contact-item">
        <span class="contact-icon"><svg width="14" height="14" viewBox="0 0 24 24"><rect x="2" y="5" width="20" height="14" rx="1.5" fill="#222"/><path d="M3 6l9 7 9-7" fill="none" stroke="#f2a81d" stroke-width="1.6"/></svg></span>
        info@kr-rangegearco.com.au
      </li>
      <li class="contact-item">
        <span class="contact-icon"><svg width="14" height="14" viewBox="0 0 24 24"><rect x="7" y="2" width="10" height="7" fill="#222"/><rect x="3" y="9" width="18" height="10" rx="1.5" fill="#222"/><rect x="7" y="15" width="10" height="7" fill="#222" stroke="#f2a81d" stroke-width="1"/></svg></span>
        +61 (0) 8 9153 2867
      </li>
    </ul>
  </section>

  <!-- Brand side -->
  <section class="card card-front" aria-label="Business card, brand side">
    <div class="pistol-photo" role="img" aria-label="Close-up photograph of a polished steel competition pistol frame and trigger guard with a textured grip"></div>
    <svg class="front-shade" width="620" height="355" viewBox="0 0 620 355" aria-hidden="true">
      <defs>
        <radialGradient id="shadeGrad" cx="0.7" cy="0.85" r="0.7">
          <stop offset="0" stop-color="#1c1d1f"/>
          <stop offset="1" stop-color="#050505"/>
        </radialGradient>
      </defs>
      <path d="M150 355 L300 175 Q430 165 620 205 V355 Z" fill="url(#shadeGrad)"/>
    </svg>
    <p class="tagline">Quality. Precision. Results</p>
    <div class="brand">
      <div class="brand-dot"></div>
      <p class="brand-name">Kyle Reeves<span>SHOOTING SUPPLIES</span></p>
    </div>
  </section>

</main>
</body>
</html>
```